New Business Cards for Organic Meat Farm

We need a business card designed for Quillendown Farm, a meat farm in western MA. Our logo uses a hand-drawn woodcut (attached). Our color palette has been simply black and white (shown in notepad and picture of our food truck). While we are based out of western MA, we have ambitions to grow nationally, so our hope is for a classy and memorable card which will be printed on a premium quality stock from a printer like printkestrel.com.
Target Market(s)
consumers of quality meats, restauranteurs, partnering farms
Industry/Entity Type
Farming and prepared meat products
Contact Information for Business Card
Wendell Pruitt, President/Owner, wendell@quillendownfarm.com, mobile: 413-555-0172, phone: 413-555-0148, quillendownfarm.com, facebook: @quillendownfarm, instagram: @quillendownfarmma
Colors
Designer to choose colors to be used in the design.
Look and feel

```html
<!DOCTYPE html>
<html lang="en">
<head>
<meta charset="utf-8">
<title>Quillendown Farm – Business Cards</title>
<link rel="stylesheet" href="https://fonts.googleapis.com/css2?family=Source+Sans+3:wght@400;700&family=Pathway+Gothic+One&display=swap">
<style>
  :root {
    --page: #fefefe;
    --card: #060807;
    --white: #ffffff;
    --gold: #d8c49c;
  }
  * { box-sizing: border-box; margin: 0; padding: 0; }
  html, body { width: 1200px; height: 1200px; overflow: hidden; background: var(--page); }
  .sheet { position: relative; width: 1200px; height: 1200px; }

  .card {
    --ink: var(--white);
    position: absolute;
    width: 483px;
    height: 268px;
    background: var(--card);
    border-radius: 14px;
    color: var(--ink);
    font-family: "Source Sans 3", sans-serif;
    overflow: hidden;
  }
  .card--gold { --ink: var(--gold); }

  .card--front-white { left: 94px;  top: 229px; }
  .card--back-white  { left: 629px; top: 228px; }
  .card--front-gold  { left: 96px;  top: 679px; }
  .card--back-gold   { left: 631px; top: 679px; }

  /* Front */
  .front-name {
    position: absolute;
    left: 0; right: 0; top: 72px;
    text-align: center;
    font-weight: 700;
    font-size: 38px;
    line-height: 42px;
  }
  .front-email {
    position: absolute;
    left: 0; right: 0; top: 219px;
    text-align: center;
    font-weight: 400;
    font-size: 19px;
    line-height: 24px;
  }

  /* Back */
  .holder {
    position: absolute;
    left: 41px; top: 44px;
    font-weight: 700;
    font-size: 22px;
    line-height: 26px;
    text-transform: uppercase;
  }
  .role {
    position: absolute;
    left: 45px; top: 72px;
    font-family: "Pathway Gothic One", sans-serif;
    font-weight: 400;
    font-size: 22px;
    line-height: 24px;
  }
  .contact-list { position: absolute; left: 47px; top: 129px; list-style: none; }
  .contact-item {
    position: relative;
    height: 28px;
    padding-left: 28px;
    font-size: 18.5px;
    line-height: 22px;
    white-space: nowrap;
  }
  .contact-item:last-child { margin-top: 5px; }
  .contact-icon {
    position: absolute;
    left: 0; top: 2px;
    width: 18px; height: 18px;
    fill: none;
    stroke: var(--ink);
    stroke-width: 1.4;
  }
  .back-name {
    position: absolute;
    left: 316px; width: 144px; top: 190px;
    text-align: center;
    font-weight: 700;
    font-size: 20px;
    line-height: 22px;
  }
</style>
</head>
<body>
<main class="sheet">

  <section class="card card--front-white">
    <div class="front-name">Quillendown<br>Farm</div>
    <p class="front-email">wendell@quillendownfarm.com</p>
  </section>

  <section class="card card--back-white">
    <h2 class="holder">Wendell Pruitt,</h2>
    <p class="role">President/Owner,</p>
    <ul class="contact-list">
      <li class="contact-item"><svg class="contact-icon" viewBox="0 0 18 18"><rect x="4.5" y="1" width="9" height="16" rx="1.5"/><line x1="7.5" y1="14.5" x2="10.5" y2="14.5"/></svg>413-555-0172,</li>
      <li class="contact-item"><svg class="contact-icon" viewBox="0 0 18 18"><path d="M4 2l3 3-1.5 2.5c1 2 2.5 3.5 4.5 4.5L12.5 10.5l3 3-2 2.5C8 15.5 2.5 10 2 4.5z"/><path d="M11 2.5a5 5 0 0 1 4.5 4.5M11 5a2.5 2.5 0 0 1 2 2"/></svg>413-555-0148,</li>
      <li class="contact-item"><svg class="contact-icon" viewBox="0 0 18 18"><circle cx="9" cy="9" r="7.5"/></svg>@quillendownfarm,</li>
      <li class="contact-item"><svg class="contact-icon" viewBox="0 0 18 18"><circle cx="9" cy="9" r="7.5"/></svg>@quillendownfarmma</li>
    </ul>
    <div class="back-name">Quillendown<br>Farm</div>
  </section>

  <section class="card card--gold card--front-gold">
    <div class="front-name">Quillendown<br>Farm</div>
    <p class="front-email">wendell@quillendownfarm.com</p>
  </section>

  <section class="card card--gold card--back-gold">
    <h2 class="holder">Wendell Pruitt,</h2>
    <p class="role">President/Owner,</p>
    <ul class="contact-list">
      <li class="contact-item"><svg class="contact-icon" viewBox="0 0 18 18"><rect x="4.5" y="1" width="9" height="16" rx="1.5"/><line x1="7.5" y1="14.5" x2="10.5" y2="14.5"/></svg>413-555-0172,</li>
      <li class="contact-item"><svg class="contact-icon" viewBox="0 0 18 18"><path d="M4 2l3 3-1.5 2.5c1 2 2.5 3.5 4.5 4.5L12.5 10.5l3 3-2 2.5C8 15.5 2.5 10 2 4.5z"/><path d="M11 2.5a5 5 0 0 1 4.5 4.5M11 5a2.5 2.5 0 0 1 2 2"/></svg>413-555-0148,</li>
      <li class="contact-item"><svg class="contact-icon" viewBox="0 0 18 18"><circle cx="9" cy="9" r="7.5"/></svg>@quillendownfarm,</li>
      <li class="contact-item"><svg class="contact-icon" viewBox="0 0 18 18"><circle cx="9" cy="9" r="7.5"/></svg>@quillendownfarmma</li>
    </ul>
    <div class="back-name">Quillendown<br>Farm</div>
  </section>

</main>
</body>
</html>
```